Business card design to promote website

SaferBlocksNow.org is a website designed for parents and other community members seeking information and other resources in the tri-county area (San Luis Obispo, Santa Barbara & Ventura Counties) about gang reduction, intervention and prevention. We are looking for a bold,eye-catching, full-color card one with a full graphic background, possibly depicting a "street" scene with police, or gang members, or dead body outline or other crime scene image. One side in English and other side in Spanish.

Target Market(s)

Parents and other community members concerned about gangs, violence, and youth & community safety

Industry/Entity Type

Business

Contact Information for Business Card

SaferBlocksNow.org
Serving San Luis Obispo, Santa Barbara & Ventura Counties

Requirements
Must have
• Design must have bold full graphic design front, and include web address. (Attached images are just inspirational; we do not own the rights to these images.) Please visit the website www.SaferBlocksNow.org to gain an understanding of the look and feel.

```html
<!DOCTYPE html>
<html lang="en">
<head>
<meta charset="utf-8">
<title>SaferBlocksNow.org – Business Cards</title>
<link rel="stylesheet" href="https://fonts.googleapis.com/css2?family=Anton&family=Archivo+Black&family=Arimo:wght@400&display=swap">
<style>
  :root {
    --page-bg: #e4e4e4;
    --card-dark: #2a2525;
    --footer-grey: #3b3b3b;
    --tape-yellow: #f6d800;
    --tape-yellow-deep: #e3b900;
    --ink: #141414;
    --url-ink: #1c1c1c;
    --tagline-yellow: #e9d418;
  }
  * { margin: 0; padding: 0; box-sizing: border-box; }
  html, body {
    width: 1200px;
    height: 900px;
    overflow: hidden;
    background: var(--page-bg);
  }
  .sheet {
    position: relative;
    width: 1200px;
    height: 900px;
  }
  .card {
    position: absolute;
    width: 622px;
    height: 366px;
    box-shadow: 6px 8px 10px rgba(0, 0, 0, 0.35);
  }
  .card--english { left: 76px; top: 50px; }
  .card--spanish { left: 452px; top: 446px; }
  .card svg { display: block; width: 100%; height: 100%; }
  .tape-words {
    font-family: "Anton", "Arial Narrow", sans-serif;
    fill: var(--ink);
  }
  .web-address {
    font-family: "Archivo Black", "Arial Black", sans-serif;
    fill: var(--url-ink);
    stroke: #8a8a8a;
    stroke-width: 0.8px;
    paint-order: stroke;
    letter-spacing: 1px;
  }
  .service-area {
    font-family: "Arimo", Arial, sans-serif;
    fill: var(--tagline-yellow);
  }
</style>
</head>
<body>
<main class="sheet">

  <section class="card card--english" aria-label="English side">
    <svg viewBox="0 0 622 366" xmlns="http://www.w3.org/2000/svg">
      <defs>
        <linearGradient id="tapeFillEn" x1="0" y1="0" x2="1" y2="0.3">
          <stop offset="0" stop-color="var(--tape-yellow)"/>
          <stop offset="1" stop-color="var(--tape-yellow-deep)"/>
        </linearGradient>
        <clipPath id="cardClipEn"><rect width="622" height="276"/></clipPath>
      </defs>
      <rect class="card-ground" width="622" height="366" fill="var(--card-dark)"/>
      <g clip-path="url(#cardClipEn)">
        <polygon class="caution-tape" points="0,0 622,128 622,276 0,276" fill="url(#tapeFillEn)"/>
        <text class="tape-words" transform="rotate(7)" x="-8" y="190" font-size="200"
              textLength="650" lengthAdjust="spacingAndGlyphs">Crime Scene Do Not</text>
      </g>
      <rect class="footer-band" y="276" width="622" height="90" fill="var(--footer-grey)"/>
      <text class="web-address" x="30" y="320" font-size="29">www.SaferBlocksNow.org</text>
      <text class="service-area" x="32" y="347" font-size="15.5">Serving San Luis Obispo, Santa Barbara &amp; Ventura Counties</text>
    </svg>
  </section>

  <section class="card card--spanish" aria-label="Spanish side" lang="es">
    <svg viewBox="0 0 622 366" xmlns="http://www.w3.org/2000/svg">
      <defs>
        <linearGradient id="tapeFillEs" x1="0" y1="0" x2="1" y2="0.3">
          <stop offset="0" stop-color="var(--tape-yellow)"/>
          <stop offset="1" stop-color="var(--tape-yellow-deep)"/>
        </linearGradient>
        <clipPath id="cardClipEs"><rect width="622" height="276"/></clipPath>
      </defs>
      <rect class="card-ground" width="622" height="366" fill="var(--card-dark)"/>
      <g clip-path="url(#cardClipEs)">
        <polygon class="caution-tape" points="0,0 622,128 622,276 0,276" fill="url(#tapeFillEs)"/>
        <text class="tape-words" transform="rotate(7)" x="-52" y="190" font-size="200"
              textLength="800" lengthAdjust="spacingAndGlyphs">Flagrante Delito¡Prohibido el paso</text>
      </g>
      <rect class="footer-band" y="276" width="622" height="90" fill="var(--footer-grey)"/>
      <text class="web-address" x="30" y="320" font-size="29">www.SaferBlocksNow.org</text>
      <text class="service-area" x="32" y="347" font-size="15.5">Se Sirve San Luis Obispo, Santa Barbara &amp; Ventura Counties</text>
    </svg>
  </section>

</main>
</body>
</html>
```